family chiropractic health care team needs a modern business card design

Healthcare office with Chiropractors, Physiotherapists, Massage therapists and possibly other practitioners in the future. This is a friendly family office with patients of all ages (and lots of kids) that just moved into a new larger modern office.
Look at the website for photos of the office.
Design for the front and back of a business card required.
Text for the front:
Office logo and name of the office:
Bright Path Wellness Centre
Name of current Practitioner:
Dr. Marten Quovel B.Sc., D.C. Chiropractor
(But please include options to swap out name and title for other practitioners )

address:
218 Farrow Gate
Larkfield NS.
K2J 6P4
Phone: 555-872-0196 (PATH)
Web site and email:
www.brightpathwellnesscentre.example
brightpathchiro@mailbox.example

2 versions of the back of the card:
1. text below
2. appointment schedule card

Text on back of card:
Chiropractic Card text on back of the card:
There is more to chiropractic than the relief of headaches and back pain! Our primary focus is the integrity of your nerve system, which controls and regulates every cell and tissue of your body. The moving bones of the spinal column can impair this vital communication link between your brain and body. We help improve the function and structure of your spine, reducing nerve system compromise. The result?
Even non-spinal related health problems can show improvement
without drugs
without surgery
regardless of age
for over a century
naturally

Appointment Card info For Back:
Please integrate design elements from the front of the card into an appointment card format.
M Tu W Th F Sat (and a line for writing on beside each one)

```html
<!DOCTYPE html>
<html lang="en">
<head>
<meta charset="utf-8">
<title>Bright Path Wellness Centre – Business Card</title>
<link rel="stylesheet" href="https://fonts.googleapis.com/css2?family=Tinos:wght@400;700&display=swap">
<style>
  :root {
    --green: #8cc152;
    --green-faint: #e6f0da;
    --grey: #7b787a;
    --ink: #1a1a1a;
    --paper: #ffffff;
    --backdrop: #d4d4d4;
  }
  * { box-sizing: border-box; margin: 0; padding: 0; }
  html, body { width: 1200px; height: 800px; overflow: hidden; }
  body {
    background: var(--backdrop);
    font-family: "Tinos", "Times New Roman", serif;
    color: var(--ink);
    display: flex;
    align-items: center;
    justify-content: center;
    gap: 40px;
  }
  .card {
    position: relative;
    width: 560px;
    height: 320px;
    background: var(--paper);
    box-shadow: 0 6px 18px rgba(0,0,0,.18);
    overflow: hidden;
  }

  /* Front */
  .card-front .edge-band {
    position: absolute; left: 0; right: 0; bottom: 0; height: 7px;
    background: linear-gradient(90deg, var(--green) 0 72%, var(--grey) 72% 100%);
  }
  .brand {
    position: absolute; top: 42px; left: 0; right: 0;
    text-align: center;
  }
  .brand-name {
    font-weight: 700;
    font-size: 34px;
    letter-spacing: 1px;
    text-transform: uppercase;
    color: var(--green);
    line-height: 1.1;
  }
  .brand-rule {
    margin: 10px auto 0;
    width: 300px; height: 1px; background: var(--grey);
  }
  .practitioner-block {
    position: absolute; top: 160px; left: 40px; right: 30px;
    display: flex; align-items: center;
  }
  .practitioner { flex: 0 0 200px; text-align: right; padding-right: 16px; }
  .practitioner-name { color: var(--green); font-weight: 700; font-size: 21px; white-space: nowrap; }
  .practitioner-title { font-size: 13px; margin-top: 3px; }
  .divider { width: 1px; height: 62px; background: var(--green); }
  .contact-list { list-style: none; padding-left: 16px; font-size: 12.5px; }
  .contact-list li { display: flex; align-items: center; gap: 7px; line-height: 20px; white-space: nowrap; }
  .contact-list svg { width: 12px; height: 12px; flex: none; }
  .address {
    position: absolute; top: 262px; left: 0; right: 0;
    text-align: center; font-size: 14px;
  }

  /* Back */
  .backdrop-name {
    position: absolute; left: 0; top: 0; bottom: 0; width: 64px;
    display: flex; align-items: center; justify-content: center;
  }
  .backdrop-name span {
    transform: rotate(-90deg);
    white-space: nowrap;
    font-weight: 700; font-size: 21px; line-height: 1.15;
    text-transform: uppercase; text-align: center;
    color: var(--green-faint); letter-spacing: 1px;
  }
  .appointment { position: absolute; top: 28px; left: 78px; right: 30px; }
  .appointment-title {
    font-weight: 700; font-size: 21px; text-transform: uppercase;
    letter-spacing: .5px; margin-bottom: 16px;
  }
  .week-row { display: flex; align-items: flex-end; margin-bottom: 17px; font-size: 14px; }
  .day { display: flex; align-items: flex-end; flex: 1; }
  .day:last-child { flex: 0 0 auto; }
  .day-label { padding-right: 3px; }
  .day-line { flex: 1; border-bottom: 1px solid var(--grey); margin: 0 6px 3px 0; }
  .datetime-row { display: flex; align-items: flex-end; gap: 12px; font-size: 15px; margin-top: 22px; }
  .datetime-row .field { display: flex; align-items: flex-end; flex: 1; }
  .datetime-row .day-line { margin-left: 6px; }
</style>
</head>
<body>

<section class="card card-front" aria-label="Business card front">
  <div class="brand">
    <div class="brand-name">Bright Path<br>Wellness Centre</div>
    <div class="brand-rule"></div>
  </div>

  <div class="practitioner-block">
    <div class="practitioner">
      <div class="practitioner-name">Dr. Marten Quovel</div>
      <div class="practitioner-title">B.Sc., D.C. Chiropractor</div>
    </div>
    <div class="divider"></div>
    <ul class="contact-list">
      <li>
        <svg viewBox="0 0 12 12"><path fill="var(--green)" d="M2.5 1l2 .3.6 2.3-1.2.9a6 6 0 0 0 3.6 3.6l.9-1.2 2.3.6.3 2a1.4 1.4 0 0 1-1.4 1.3A9.5 9.5 0 0 1 1 2.4 1.4 1.4 0 0 1 2.5 1z"/></svg>
        555-872-0196 (PATH)
      </li>
      <li>
        <svg viewBox="0 0 12 12"><rect x="1" y="2.5" width="10" height="7" fill="var(--green)"/><path d="M1 2.5l5 4 5-4" fill="none" stroke="#fff" stroke-width="1"/></svg>
        brightpathchiro@mailbox.example
      </li>
      <li>
        <svg viewBox="0 0 12 12" fill="none" stroke="var(--green)" stroke-width="1.1"><circle cx="6" cy="6" r="5"/><ellipse cx="6" cy="6" rx="2.2" ry="5"/><path d="M1 6h10M2 3.5h8M2 8.5h8"/></svg>
        www.brightpathwellnesscentre.example
      </li>
    </ul>
  </div>

  <div class="address">218 Farrow Gate Larkfield NS K2J 6P4</div>
  <div class="edge-band"></div>
</section>

<section class="card card-back" aria-label="Appointment card back">
  <div class="backdrop-name"><span>Bright Path<br>Wellness Centre</span></div>

  <div class="appointment">
    <h2 class="appointment-title">Your Next Appointment</h2>

    <div class="week-row">
      <span class="day"><span class="day-label">M</span><span class="day-line"></span></span>
      <span class="day"><span class="day-label">T</span><span class="day-line"></span></span>
      <span class="day"><span class="day-label">W</span><span class="day-line"></span></span>
      <span class="day"><span class="day-label">TH</span><span class="day-line"></span></span>
      <span class="day"><span class="day-label">FRI</span><span class="day-line"></span></span>
      <span class="day"><span class="day-label">SAT</span></span>
    </div>
    <div class="week-row">
      <span class="day"><span class="day-label">M</span><span class="day-line"></span></span>
      <span class="day"><span class="day-label">T</span><span class="day-line"></span></span>
      <span class="day"><span class="day-label">W</span><span class="day-line"></span></span>
      <span class="day"><span class="day-label">TH</span><span class="day-line"></span></span>
      <span class="day"><span class="day-label">FRI</span><span class="day-line"></span></span>
      <span class="day"><span class="day-label">SAT</span></span>
    </div>
    <div class="week-row">
      <span class="day"><span class="day-label">M</span><span class="day-line"></span></span>
      <span class="day"><span class="day-label">T</span><span class="day-line"></span></span>
      <span class="day"><span class="day-label">W</span><span class="day-line"></span></span>
      <span class="day"><span class="day-label">TH</span><span class="day-line"></span></span>
      <span class="day"><span class="day-label">FRI</span><span class="day-line"></span></span>
      <span class="day"><span class="day-label">SAT</span></span>
    </div>
    <div class="week-row">
      <span class="day"><span class="day-label">M</span><span class="day-line"></span></span>
      <span class="day"><span class="day-label">T</span><span class="day-line"></span></span>
      <span class="day"><span class="day-label">W</span><span class="day-line"></span></span>
      <span class="day"><span class="day-label">TH</span><span class="day-line"></span></span>
      <span class="day"><span class="day-label">FRI</span><span class="day-line"></span></span>
      <span class="day"><span class="day-label">SAT</span></span>
    </div>

    <div class="datetime-row">
      <span class="field">DATE<span class="day-line"></span></span>
      <span class="field">TIME<span class="day-line"></span></span>
    </div>
  </div>
</section>

</body>
</html>
```